Business Card for Language School (2 locations)

We need a sleek business card for a language school that is looking to update our image to be more professional. We work with students ages Pre-Kindergarten through adults. Our idea is to have an all-black business card with white or silver lettering. On the front will be the name of our school (Bright Maple English Academy), and on the back there will be information for our location, phone number, email, and website (and possibly social media information). We have two school branches, so the address, phone number, and email address will be different for each branch, but all of the other information will stay the same. We'd like each branch to have a different color card edge that is neon. We are also open to suggestions and new ideas!

Some answers to questions we have received:
1. The reason we haven't added a logo is because we are looking to get a new one. We hadn't originally planned to do that at this time, but we are going to look into updating our project to include that as another aspect of it. We had previously planned to just include the school name on the front without a logo at this time.
2. We currently have two branches of our school, and we want our business card design to be uniform for each location. While it might make sense to put the information on one card right now, we plan to have more locations in the future, so we want to plan ahead with a unified design right now.
3. Our school addresses and phone numbers can be found on our website: www.brightmapleenglish.example (at the bottom of the page)!
Updates

Part of this contest is also a new logo design. Our previous design was a train, which we would be open to keeping if it had an updated, sleeker design.

Contact Information for Business Card

Card #1:
Bright Maple English Academy (Qiaolin Branch)
Yuqing W. Rd. Sec. 3, Lane 412, No. 29, 1F
Beitou District, Taipei City 11268
02-2649-3058
qiaolin@brightmapleenglish.example

Card #2:
Bright Maple English Academy (Fenghe Branch)
Fulan Road, No. 318, 1F
Songshan District, Taipei City 10573
02-2761-4402
fenghe@brightmapleenglish.example

Both cards:
Website: www.brightmapleenglish.example
Facebook: www.facebook.com/brightmapleenglish
Instagram: @brightmapleenglish

```html
<!DOCTYPE html>
<html lang="en">
<head>
<meta charset="utf-8">
<title>Bright Maple English Academy – Fenghe Branch Business Card</title>
<link href="https://fonts.googleapis.com/css2?family=Roboto:wght@400&family=Noto+Sans+TC:wght@400&display=swap" rel="stylesheet">
<style>
  :root {
    --backdrop: #2b2b2b;
    --card: #121212;
    --silver: #cfcfcf;
    --ink: #f2f2f2;
    --rule: #bdbdbd;
    --edge-neon: #39ff88;
  }
  * { box-sizing: border-box; margin: 0; padding: 0; }
  html, body { width: 1200px; height: 1200px; overflow: hidden; }
  body {
    background: var(--backdrop);
    font-family: "Roboto", Arial, sans-serif;
    color: var(--ink);
    position: relative;
  }
  .card {
    position: absolute;
    left: 220px;
    width: 760px;
    height: 434px;
    background: var(--card);
    border: 3px solid var(--edge-neon);
    box-shadow: 0 0 10px rgba(57,255,136,.45), 0 8px 24px rgba(0,0,0,.45);
  }
  .card--front { top: 150px; }
  .card--back  { top: 620px; }

  .school-name {
    font-family: "Roboto", Arial, sans-serif;
    font-weight: 400;
    color: var(--silver);
    font-size: 36px;
    line-height: 1.2;
    white-space: nowrap;
  }
  .card--front .school-name {
    position: absolute;
    left: 50%; top: 50%;
    transform: translate(-50%, -50%);
  }
  .card--back .school-name {
    position: absolute;
    left: 53px; top: 62px;
  }

  .divider {
    position: absolute;
    left: 53px; right: 53px; top: 211px;
    height: 1px;
    background: var(--rule);
  }

  .contact-list {
    list-style: none;
    position: absolute;
    left: 53px; top: 237px;
    font-size: 19px;
  }
  .contact-list li {
    display: flex; align-items: center;
    height: 30px;
  }
  .contact-list svg { width: 18px; height: 18px; margin-right: 14px; flex: none; }

  .branch-address {
    position: absolute;
    right: 53px; bottom: 37px;
    text-align: right;
    font-size: 19px;
    line-height: 1.35;
    font-style: normal;
  }
  .branch-address__zh {
    margin-top: 10px;
    font-family: "Noto Sans TC", sans-serif;
  }
</style>
</head>
<body>

<section class="card card--front">
  <p class="school-name">Bright Maple English Academy</p>
</section>

<section class="card card--back">
  <p class="school-name">Bright Maple English Academy</p>

  <div class="divider"></div>

  <ul class="contact-list">
    <li>
      <svg viewBox="0 0 24 24" aria-hidden="true"><path fill="#f2f2f2" d="M6.6 10.8a15 15 0 0 0 6.6 6.6l2.2-2.2c.3-.3.7-.4 1-.2 1.1.4 2.3.6 3.6.6.6 0 1 .4 1 1V20c0 .6-.4 1-1 1A17 17 0 0 1 3 4c0-.6.4-1 1-1h3.5c.6 0 1 .4 1 1 0 1.3.2 2.5.6 3.6.1.3 0 .7-.2 1z"/></svg>
      02-2761-4402
    </li>
    <li>
      <svg viewBox="0 0 24 24" aria-hidden="true"><rect x="2.5" y="5" width="19" height="14" fill="none" stroke="#f2f2f2" stroke-width="2"/><path d="M3 6l9 7 9-7" fill="none" stroke="#f2f2f2" stroke-width="2"/></svg>
      fenghe@brightmapleenglish.example
    </li>
    <li>
      <svg viewBox="0 0 24 24" aria-hidden="true"><g fill="none" stroke="#f2f2f2" stroke-width="1.6"><circle cx="12" cy="12" r="9.5"/><ellipse cx="12" cy="12" rx="4" ry="9.5"/><path d="M2.5 12h19M4 7h16M4 17h16"/></g></svg>
      www.brightmapleenglish.example
    </li>
    <li>
      <svg viewBox="0 0 24 24" aria-hidden="true"><circle cx="12" cy="12" r="8" fill="none" stroke="#f2f2f2" stroke-width="2"/></svg>
      brightmapleenglish.example
    </li>
    <li>
      <svg viewBox="0 0 24 24" aria-hidden="true"><rect x="4" y="4" width="16" height="16" fill="none" stroke="#f2f2f2" stroke-width="2"/></svg>
      @brightmapleenglish
    </li>
  </ul>

  <address class="branch-address">
    <div>Fenghe Branch</div>
    <div>1F, No.318, Fulan Rd</div>
    <div>Songshan District</div>
    <div class="branch-address__zh">台北市松山區富蘭路<br>318號1樓</div>
  </address>
</section>

</body>
</html>
```